Brick and Mortar Store front design for Rosalind & Beatrix's Boutique THIS IS NOT JUST A SIGN

We are on the hunt for a cutting-edge design that will transform our brick and mortar store front into a modern and chic space that exudes energy and captures attention. As ambitious young female entrepreneurs with a passion for fashion and design, we want our storefront to reflect our unique personality and style.

One of the main elements we seek in the design is a sense of freshness that makes the space feel lively and vibrant, while also offering a distinctive and unforgettable style. Although the building's current color scheme is black, we are open to exploring different color options to create a dynamic and engaging atmosphere. We have even provided photos of design ideas that appeal to us.

Our ultimate goal is to attract shoppers who crave the latest trends and styles in fashion. Therefore, we need a design that is not only stunning but also eye-catching. The outside of our storefront boasts a lot of depth and textures, which we want to incorporate into the design to create a cohesive and visually impressive display.

We are excited to collaborate with a designer who shares our vision and can help bring our ideas to life. Our dream is to create a store front that accurately reflects our love for fashion and design and serves as a shining beacon for young women seeking the latest trends and styles.

(colours we like... bright colours, black, white.. ). Also attaching our logo

This is about colour of the building (do we paint it another vibrant colour, do we paint the spaces that are framed out, signage on the top should it be gold or a colour, windows need to be able to be looked through but maybe. Some elegant peony’s around the edges)

www.rosalind-beatrixes.example

Target Market(s)

Women aged 16-60

Industry/Entity Type

Women's Boutique, Shopping, retail

Colors
00AB8E
00BBA5
67D7C9
C6EFE9
E9F9F6
FFC000
F8CF3A
FAE287
FDF2CF
FEFAEE
F0912C
F2A743
F7CA91
FBE8D2
FDF5EE
E54698
E96AAD
F1A4CE
F9D9EA
FCEFF6
A7469A
B969AE
D3A5CF
EDDBEB
F8F0F9

Requirements
Must have
• Clear detailed designs, showing colours and style that are outlined in the brief. I have attached different versions of the logo. We only need one logo style not them all
Nice to have
• Please see the design brief
Should not have
• nothing plain Jane NOT just stickers in the windows we are looking for all over nee design please read the brief thoroughly before submitting. Look at the photo examples. It is about paint colour signage lights etc.

```html
<!DOCTYPE html>
<html lang="en">
<head>
<meta charset="utf-8">
<title>Rosalind &amp; Beatrix's Boutique – Storefront</title>
<link rel="stylesheet" href="https://fonts.googleapis.com/css2?family=Crimson+Pro:wght@600&family=Playfair+Display:wght@800&family=Montserrat:wght@500;700&display=swap">
<style>
  :root {
    --facade: #1f1f1f;
    --facade-line: #2e2e2e;
    --ink: #111111;
    --sign-pink: #f6d3da;
    --panel-pink: #f8d6df;
    --soft-pink: #fbe3ea;
    --peony: #ec8d92;
    --rose: #e97a8e;
    --peach: #f5a878;
    --copper: #e08a4f;
    --magenta: #c2185b;
    --white: #ffffff;
    --glass: #b9bcc4;
    --band-text: #f4a0a6;
  }
  * { box-sizing: border-box; margin: 0; padding: 0; }
  html, body { width: 1200px; height: 749px; overflow: hidden; }
  body { background: var(--facade); position: relative; font-family: "Montserrat", sans-serif; }

  .abs { position: absolute; }

  /* Top fascia sign */
  .fascia { left: 134px; top: 113px; width: 929px; height: 127px; background: var(--sign-pink); overflow: hidden; }
  .fascia__blob { position: absolute; border-radius: 50%; background: var(--peach); }
  .fascia__bouquet { position: absolute; top: 13px; width: 92px; height: 112px; border-radius: 46px 46px 10px 10px;
    background: linear-gradient(180deg, var(--peony) 0%, #d9737c 60%, #3a2a2c 100%); }
  .fascia__name { position: absolute; left: 330px; width: 270px; top: 18px; text-align: center;
    font-family: "Playfair Display", serif; font-weight: 800; color: var(--ink); line-height: 1; }
  .fascia__name-top { display: block; font-size: 44px; }
  .fascia__name-bottom { display: block; font-size: 30px; margin-top: 6px; }

  /* Boutique band */
  .band { left: 248px; top: 331px; width: 732px; height: 69px; background: var(--ink); overflow: hidden; }
  .band__title { position: absolute; left: 0; right: 0; top: 10px; text-align: center;
    font-family: "Crimson Pro", serif; font-weight: 600; font-size: 38px; color: var(--band-text); }
  .band__sprig { position: absolute; }

  /* Shop windows */
  .window { overflow: hidden; }
  .window--bouquet { left: 206px; top: 454px; width: 98px; height: 199px; background: var(--panel-pink); }
  .window--brand { left: 313px; top: 454px; width: 153px; height: 196px; background: var(--white); }
  .window--figure { left: 477px; top: 452px; width: 156px; height: 198px; background: var(--panel-pink); }
  .window--figure-right { left: 862px; top: 450px; width: 159px; height: 197px; background: var(--panel-pink); }

  .art { position: absolute; }

  .brand__name { position: absolute; left: 0; right: 0; top: 70px; text-align: center;
    font-family: "Playfair Display", serif; font-weight: 800; font-size: 14px; color: var(--ink); line-height: 1.1; }
  .brand__fashion { position: absolute; left: 0; right: 0; top: 132px; text-align: center;
    font-weight: 700; font-size: 17px; letter-spacing: 1px; color: var(--peach); }
  .brand__blurb { position: absolute; left: 24px; right: 24px; top: 156px; text-align: center;
    font-size: 3.2px; line-height: 1.35; color: var(--rose); font-weight: 500; }

  .figure__word { position: absolute; left: 8px; top: 150px; transform: rotate(-90deg); transform-origin: left top;
    font-weight: 700; font-size: 24px; letter-spacing: 1px; color: #f3bccb; }

  .right__name { position: absolute; left: 70px; top: 70px; width: 84px; text-align: center;
    font-family: "Playfair Display", serif; font-weight: 800; font-size: 8px; color: var(--ink); }

  /* Doors */
  .doors { left: 644px; top: 448px; width: 211px; height: 241px; background: #181818; border: 2px solid var(--facade-line); }
  .door__glass { position: absolute; top: 23px; width: 70px; height: 146px; background: linear-gradient(180deg, #c6d4e6 0%, var(--glass) 45%, #8f8b8e 100%); }
  .door__glass--left { left: 12px; }
  .door__glass--right { left: 119px; }
  .door__kick { position: absolute; top: 192px; width: 76px; height: 20px; border: 2px solid var(--facade-line); }
  .door__oval { position: absolute; left: 10px; top: 35px; width: 49px; height: 85px; border-radius: 50%; background: var(--soft-pink);
    display: flex; align-items: center; justify-content: center; text-align: center;
    font-family: "Playfair Display", serif; font-weight: 800; font-size: 6px; color: var(--ink); line-height: 1.2; }
  .hours { position: absolute; left: 4px; right: 4px; top: 52px; text-align: center; color: var(--white);
    font-size: 2.6px; line-height: 1.35; font-weight: 500; }
  .hours__head { font-weight: 700; font-size: 2.8px; margin-top: 2px; }
  .door__handle { position: absolute; top: 100px; width: 3px; height: 16px; background: #9a9a9a; }
</style>
</head>
<body>

  <!-- Top fascia -->
  <section class="fascia abs" aria-label="Main fascia sign">
    <span class="fascia__blob" style="left:45px; top:-25px; width:60px; height:60px;"></span>
    <span class="fascia__blob" style="left:828px; top:98px; width:70px; height:60px;"></span>
    <div class="fascia__bouquet" style="left:220px;" role="img" aria-label="Pink peony bouquet illustration"></div>
    <div class="fascia__name">
      <span class="fascia__name-top">Rosalind</span>
      <span class="fascia__name-bottom">&amp; Beatrix's</span>
    </div>
    <div class="fascia__bouquet" style="left:617px;" role="img" aria-label="Pink peony bouquet illustration"></div>
  </section>

  <!-- Boutique name band -->
  <section class="band abs" aria-label="Boutique name band">
    <div class="band__sprig" style="left:2px; top:2px; width:70px; height:40px; background:linear-gradient(135deg,#f5b08a,#d98a55); border-radius:0 0 40px 0;" role="img" aria-label="Peach leaf sprig illustration"></div>
    <div class="band__title">Rosalind &amp; Beatrix's Boutique</div>
    <div class="band__sprig" style="right:0; top:0; width:66px; height:69px; background:linear-gradient(200deg,#f7c3cc,#ec8d9a); border-radius:40px 0 0 0;" role="img" aria-label="Pink leaf sprig illustration"></div>
  </section>

  <!-- Window 1 -->
  <section class="window window--bouquet abs" aria-label="Window graphic">
    <span class="art" style="left:42px; top:-10px; width:70px; height:50px; border-radius:50%; background:var(--peach);"></span>
    <div class="art" style="left:0; top:72px; width:98px; height:90px; background:var(--white); border-radius:0 40px 40px 0;"></div>
    <div class="art" style="left:18px; top:90px; width:58px; height:68px; border-radius:28px 28px 8px 8px; background:linear-gradient(180deg,var(--peony),#3a2a2c);" role="img" aria-label="Peony bouquet illustration"></div>
  </section>

  <!-- Window 2 -->
  <section class="window window--brand abs" aria-label="Brand window poster">
    <span class="art" style="left:0; top:55px; width:72px; height:40px; border-radius:50%; background:var(--sign-pink);"></span>
    <div class="art" style="left:18px; top:56px; width:30px; height:38px; border-radius:15px 15px 4px 4px; background:linear-gradient(180deg,var(--peony),#3a2a2c);" role="img" aria-label="Small peony bouquet illustration"></div>
    <div class="brand__name" style="left:44px;">Rosalind<br>&amp; Beatrix's</div>
    <div class="brand__fashion">FASHION</div>
    <p class="brand__blurb">Fresh pieces arrive every week in soft colours and bold cuts, picked for women who love new looks and easy style every day.</p>
  </section>

  <!-- Window 3 -->
  <section class="window window--figure abs" aria-label="Fashion window poster">
    <div class="figure__word">FASHION</div>
    <div class="art" style="left:22px; top:14px; width:98px; height:176px; background:linear-gradient(180deg,#f2c9d3 0%,var(--white) 45%,#f3d9df 100%); border-radius:40px 40px 6px 6px;" role="img" aria-label="Illustration of a woman in a white dress"></div>
    <span class="art" style="left:100px; top:117px; width:24px; height:22px; border-radius:50%; background:var(--copper);"></span>
    <span class="art" style="left:118px; top:142px; width:70px; height:70px; border-radius:50%; border:14px solid var(--copper);"></span>
  </section>

  <!-- Doors -->
  <section class="doors abs" aria-label="Entrance doors">
    <div class="door__glass door__glass--left">
      <div class="door__oval">Rosalind<br>&amp;<br>Beatrix's</div>
    </div>
    <span class="door__handle" style="left:89px;"></span>
    <span class="door__handle" style="left:110px;"></span>
    <div class="door__glass door__glass--right">
      <div class="hours">
        <div class="hours__head">WE'RE OPEN</div>
        <div>Most days about 9:00 or 10:00</div>
        <div>Some days as early as 8:00, others as late as noon</div>
        <div class="hours__head">WE'RE CLOSED</div>
        <div>About 5:30 or 6:00</div>
        <div>Sometimes 4:00 or 5:00, some days as late as 9:00</div>
        <div>Some days we aren't here at all, lately we're here all the time</div>
      </div>
    </div>
    <span class="door__kick" style="left:10px;"></span>
    <span class="door__kick" style="left:117px;"></span>
  </section>

  <!-- Window 4 -->
  <section class="window window--figure-right abs" aria-label="Fashion window poster">
    <span class="art" style="left:20px; top:-12px; width:62px; height:44px; border-radius:50%; background:var(--peach);"></span>
    <div class="art" style="left:20px; top:44px; width:46px; height:146px; border-radius:22px 22px 6px 6px; background:linear-gradient(180deg,#f2c9d3 0%,var(--white) 35%,var(--magenta) 55%,#f3d9df 80%);" role="img" aria-label="Illustration of a woman in a white top and magenta skirt"></div>
    <span class="art" style="left:70px; top:60px; width:70px; height:70px; border-radius:50%; border:1px solid #555;"></span>
    <div class="right__name" style="left:66px; top:56px; width:78px;">Rosalind &amp; Beatrix's</div>
    <div class="art" style="left:88px; top:84px; width:34px; height:40px; border-radius:16px 16px 4px 4px; background:linear-gradient(180deg,var(--peony),#3a2a2c);" role="img" aria-label="Small peony bouquet illustration"></div>
    <span class="art" style="left:136px; top:140px; width:40px; height:60px; border-radius:50%; background:var(--copper);"></span>
  </section>

</body>
</html>
```